Talvora Companies Business Card Design

We need a new business card for our Private Equity Real Estate Development firm, “Talvora” and our EB-5 regional center “Mossgate Regional Center” on one card. We prefer a design that is simple, elegant, and represents the luxury products we design and build as well as the financial security and stability our successful history has produced. We are an industry leader in our field and 3rd generation family business that has evolved into an institutional quality investment platform. Considered design size is standard business card dimensions (3.5 x 2 inches with an additional 1/8 inch space for design elements or backgrounds that extend beyond the finished size of your piece.

Target Market(s)

• High net worth individuals
• Highly skilled technical workers and physicians in the US seeking investment-based immigration opportunities
• Sophisticated private equity investors
• Intermediary partners include domestic attorneys and investment brokers, as well as international agent networks
• US real estate developers

Industry/Entity Type

Finance

Contact Information for Business Card

(Providing placeholder info for personal information, please design for longer character spaces, longer names and addresses etc..)
• Logo for Talvora
• Logo for Mossgate Regional Center
• Full name: Dermot Talvora
• Job title: CEO
• Email address: dtalvora@talvoracompanies.com
• Cell phone number: +1.555.314.2786
• Office number +1.555.862.4071
• Office address: Quillfield Park 7, 4817 Vista Loma, Alder Vale, CA.
• Website: www.talvoracompanies.com

Font styles to use
Serif
Sans Serif

Colors
ec1f27
ffffff
000000

Requirements
Must have
• • Logo for Talvora
• • Logo for Mossgate Regional Center
• - Use rounded corners
• (See .ai file included for logos)
Nice to have
• • Simple, elegant design
• • Aesthetically compatible with our website design (www.talvoracompanies.com)
• • Color palette including but not limited to white, black, and red (as per logos)
Should not have
• - Not too much red color
• - Do not stack both logos on top of each other

```html
<!DOCTYPE html>
<html lang="en">
<head>
<meta charset="utf-8">
<title>Mossgate Regional Center – Business Card</title>
<link rel="stylesheet" href="https://fonts.googleapis.com/css2?family=Tinos:wght@400;700&display=swap">
<style>
  :root {
    --bg: #202022;
    --brand-red: #a51e36;
    --paper: #ffffff;
    --ink: #2d3440;
    --slate: #5c6472;
    --rule: #3a4250;
  }
  * { margin: 0; padding: 0; box-sizing: border-box; }
  html, body { width: 1200px; height: 880px; overflow: hidden; }
  body {
    background: var(--bg);
    font-family: "Tinos", "Times New Roman", serif;
    position: relative;
  }
  .card {
    position: absolute;
    width: 560px;
    height: 320px;
    border-radius: 18px;
    overflow: hidden;
  }
  .card--back { left: 70px; top: 80px; background: var(--brand-red); }
  .card--front { left: 570px; top: 480px; background: var(--paper); }

  .wordmark {
    position: absolute;
    display: flex;
    flex-direction: column;
    line-height: 1;
    font-weight: 700;
  }
  .wordmark__name { font-size: 44px; letter-spacing: 1px; }
  .wordmark__sub { font-size: 11px; letter-spacing: 7.4px; margin-top: 8px; }

  .card--back .wordmark {
    left: 50%; top: 50%;
    transform: translate(-50%, -50%);
    color: var(--paper);
    align-items: center;
  }

  .card--front .wordmark { left: 40px; top: 62px; color: var(--brand-red); }
  .card--front .wordmark__name { font-size: 38px; }
  .card--front .wordmark__sub { font-size: 10px; letter-spacing: 6.6px; margin-top: 7px; }

  .divider {
    position: absolute;
    left: 200px; right: 30px; top: 176px;
    height: 1px; background: var(--rule);
  }

  .person { position: absolute; left: 30px; top: 160px; }
  .person__name { font-size: 18px; font-weight: 700; color: var(--brand-red); }
  .person__title { font-size: 13px; color: var(--slate); margin-top: -2px; }

  .contacts { position: absolute; left: 30px; top: 208px; list-style: none; }
  .contacts li {
    display: flex; align-items: center; gap: 7px;
    font-size: 12.5px; color: var(--ink); line-height: 16px;
  }
  .contacts svg { width: 11px; height: 11px; flex: none; }

  .address {
    position: absolute; right: 40px; top: 186px;
    text-align: right; font-size: 12.5px; line-height: 15px; color: var(--ink);
    font-style: normal;
  }

  .bands { position: absolute; left: 0; bottom: 0; width: 560px; height: 44px; }
  .website {
    position: absolute; right: 24px; bottom: 13px;
    font-size: 12px; color: var(--paper); letter-spacing: 0.3px;
  }
</style>
</head>
<body>

<section class="card card--back" aria-label="Card back">
  <div class="wordmark">
    <span class="wordmark__name">MOSSGATE</span>
    <span class="wordmark__sub">REGIONAL CENTER</span>
  </div>
</section>

<section class="card card--front" aria-label="Card front">
  <div class="wordmark">
    <span class="wordmark__name">MOSSGATE</span>
    <span class="wordmark__sub">REGIONAL CENTER</span>
  </div>

  <div class="divider"></div>

  <div class="person">
    <div class="person__name">Dermot Talvora</div>
    <div class="person__title">CEO</div>
  </div>

  <ul class="contacts">
    <li>
      <svg viewBox="0 0 12 12"><rect x="3" y="0.8" width="6" height="10.4" rx="1" fill="none" stroke="var(--brand-red)" stroke-width="1.3"/></svg>
      +1.555.314.2786
    </li>
    <li>
      <svg viewBox="0 0 12 12"><path d="M1 4 Q6 0 11 4 L9.5 5.5 L8 4.3 L4 4.3 L2.5 5.5 Z M3 6 H9 L10 11 H2 Z" fill="var(--brand-red)"/></svg>
      +1.555.862.4071
    </li>
    <li>
      <svg viewBox="0 0 12 12"><rect x="0.5" y="2.5" width="11" height="7.5" fill="var(--brand-red)"/><path d="M0.5 2.5 L6 7 L11.5 2.5" fill="none" stroke="#fff" stroke-width="0.9"/></svg>
      dtalvora@talvoracompanies.com
    </li>
  </ul>

  <address class="address">
    Quillfield Park 7<br>
    4817 Vista Loma<br>
    Alder Vale, CA.
  </address>

  <svg class="bands" viewBox="0 0 560 44" preserveAspectRatio="none" aria-hidden="true">
    <polygon points="0,22 306,22 296,44 0,44" fill="var(--slate)"/>
    <polygon points="314,0 560,0 560,44 300,44" fill="var(--brand-red)"/>
  </svg>
  <div class="website">www.talvoracompanies.com</div>
</section>

</body>
</html>
```